Webpage needed for a new legal recruitment/headhunting companyi

I would like a professional and sharp looking website to showcase a new legal headhunting/recruitment company called Ridgel. The logo for the company is attached.

I like the following websites:
http://www.brimvaleadvisory.co.uk/
(For the general style and layout- although photographs of the team will be difficult as we don't have one yet!;-))

http://qomd.co.uk/
I like the style of the photographs etc on this one.

NB the pictures attached below are for information only- I don't think I would be able to use any of them...

Hope you can help!
Many thanks

```html
<!DOCTYPE html>
<html lang="en">
<head>
<meta charset="utf-8">
<title>Ridgel Legal Recruitment</title>
<link rel="stylesheet" href="https://fonts.googleapis.com/css2?family=Open+Sans:wght@400;600&display=swap">
<style>
:root{
  --purple:#4b2d72;
  --purple-panel:rgba(72,40,110,.93);
  --orange:#f7941d;
  --text:#5a5a5a;
  --heading:#3f3f3f;
  --muted:#7a7a7a;
  --rule:#d6d6d6;
  --page:#f2f2f2;
  --footer:#ececec;
  --white:#ffffff;
}
*{margin:0;padding:0;box-sizing:border-box}
html,body{width:1200px;height:1033px;overflow:hidden}
body{position:relative;background:var(--page);font-family:"Open Sans",Arial,sans-serif;color:var(--text)}
.abs{position:absolute}

.site-header{left:0;top:0;width:1200px;height:121px;background:var(--white);border-bottom:1px solid #e2e2e2}
.contact-strip{right:133px;top:10px;padding:0 0 8px 0;width:301px;border-bottom:1px solid #dcdcdc;font-size:13px;color:var(--muted);display:flex;justify-content:flex-end;align-items:center;gap:6px;white-space:nowrap}
.contact-strip svg{flex:none}
.brand{left:155px;top:42px;display:flex;align-items:center;gap:10px;font-size:40px;font-weight:400;color:var(--purple);letter-spacing:1px;line-height:1}
.brand-dot{width:22px;height:22px;border-radius:50%;background:var(--purple)}
.main-nav{right:133px;top:84px;display:flex;list-style:none}
.main-nav li{font-size:16px;color:#8a8a8a;padding:0 17px;height:36px;line-height:36px;white-space:nowrap}
.main-nav li:last-child{padding-right:0}
.main-nav li.active{background:var(--orange);color:var(--white);font-weight:600;margin:0 4px}

.hero{left:146px;top:143px;width:924px;height:333px;border-radius:3px;overflow:hidden}
.hero-photo{position:absolute;inset:0;background:linear-gradient(180deg,#d8d8d8 0%,#a9a9a9 35%,#6d6d6d 70%,#4e4e4e 100%)}
.hero-panel{left:456px;top:97px;width:395px;height:170px;background:var(--purple-panel);padding:22px 35px}
.hero-panel h1{font-size:31px;font-weight:600;line-height:36px;color:var(--white)}
.search-row{position:absolute;left:35px;top:112px;display:flex;gap:11px}
.search-field{width:236px;height:32px;background:var(--white);border-radius:2px;font-size:13.5px;color:#888;padding:6px 12px;display:flex;justify-content:space-between;align-items:center}
.search-btn{width:81px;height:32px;background:var(--orange);color:var(--white);font-size:14px;font-weight:600;text-align:center;line-height:32px;border-radius:2px}

.side-nav{left:150px;top:520px;width:144px;list-style:none}
.side-nav li{height:37.5px;border-bottom:1px solid var(--rule);display:flex;align-items:center;gap:14px;font-size:15px;color:var(--purple);padding-left:3px;white-space:nowrap}
.side-nav li:last-child{border-bottom:none}
.side-nav svg{width:13px;height:13px;fill:var(--purple);flex:none}
.book-art{left:146px;top:722px;width:122px;height:126px;border-radius:6px;background:linear-gradient(135deg,#5a5a5a,#2a2a2a 60%,#8b5a2b);transform:rotate(-8deg);z-index:2}

.welcome{left:349px;top:516px;width:436px}
.welcome h2,.featured h2{font-size:23px;font-weight:400;color:var(--heading);margin-bottom:11px;white-space:nowrap}
.welcome p{font-size:13.6px;line-height:21.5px;margin-bottom:21.5px}

.featured{left:834px;top:516px;width:212px}
.featured h2{margin-left:2px}
.job{height:61px;border-bottom:1px solid var(--rule);padding-top:2px}
.job + .job{padding-top:10px}
.job:last-child{border-bottom:none}
.job-title{font-size:13px;color:var(--text);line-height:20px;white-space:nowrap}
.job-loc{font-size:12.3px;color:var(--muted);display:flex;align-items:center;gap:3px;margin-top:1px}
.job-loc svg{width:8px;height:11px;fill:#888}

.site-footer{left:0;top:818px;width:1200px;height:168px;background:var(--footer);border-top:1px solid #e0e0e0}
.footer-brand{left:157px;top:890px;display:flex;align-items:center;gap:8px;font-size:34px;color:#a5a5a5;line-height:1}
.footer-brand .brand-dot{width:18px;height:18px;background:#a5a5a5}
.quick-links{left:361px;top:842px}
.quick-links h3{font-size:14px;font-weight:600;color:var(--heading);margin-bottom:8px}
.link-cols{display:flex}
.link-cols ul{list-style:none;width:201px}
.link-cols li{font-size:12.8px;line-height:21.5px;color:var(--muted);white-space:nowrap}
.map-art{left:905px;top:819px;width:196px;height:114px;background:radial-gradient(ellipse at center,rgba(205,205,205,.35),rgba(236,236,236,0) 70%)}
.footer-contact{left:832px;top:840px}
.footer-contact h3{font-size:20px;font-weight:400;color:var(--heading);display:flex;align-items:center;gap:9px;margin-bottom:6px}
.footer-contact h3 svg{width:19px;height:15px}
.footer-contact p{font-size:13px;line-height:21.5px;color:var(--muted);white-space:nowrap}
.footer-contact .write{color:var(--purple);text-decoration:underline}
.footer-contact .gap{margin-top:4px}

.legal-bar{left:0;top:986px;width:1200px;height:47px;border-top:1px solid #d8d8d8;background:var(--footer);text-align:center;font-size:14px;line-height:46px;color:var(--text)}
</style>
</head>
<body>

<header class="site-header abs">
  <div class="contact-strip abs">
    <svg width="12" height="12" viewBox="0 0 24 24" fill="#777"><path d="M6.6 10.8a15.1 15.1 0 0 0 6.6 6.6l2.2-2.2c.3-.3.7-.4 1-.2 1.1.4 2.3.6 3.6.6.6 0 1 .4 1 1V20c0 .6-.4 1-1 1C10.6 21 3 13.4 3 4c0-.6.4-1 1-1h3.5c.6 0 1 .4 1 1 0 1.3.2 2.5.6 3.6.1.3 0 .7-.2 1z"/></svg>
    <span>Tel: +44 20 7946 0381,&nbsp;&nbsp; Fax: +44 870 555 0194</span>
  </div>
  <div class="brand abs"><span class="brand-dot"></span><span>Ridgel</span></div>
  <ul class="main-nav abs">
    <li>Consultancy</li>
    <li class="active">Candidates</li>
    <li>clients</li>
    <li>Your Team</li>
    <li>Advice</li>
    <li>Contact Us</li>
  </ul>
</header>

<section class="hero abs">
  <div class="hero-photo" role="img" aria-label="Black and white aerial photograph of a city skyline with skyscrapers"></div>
  <div class="hero-panel abs">
    <h1>Excellence in Legal Recruiting</h1>
    <div class="search-row">
      <div class="search-field"><span>Search Vacancies</span>
        <svg width="16" height="16" viewBox="0 0 24 24" fill="none" stroke="#999" stroke-width="2.5"><circle cx="10" cy="10" r="7"/><path d="M15 15l6 6"/></svg>
      </div>
      <div class="search-btn">SEARCH</div>
    </div>
  </div>
</section>

<ul class="side-nav abs">
  <li><svg viewBox="0 0 24 24"><path d="M10 2a8 8 0 0 1 6.3 12.9l5.4 5.4-2.1 2.1-5.4-5.4A8 8 0 1 1 10 2zm0 3a5 5 0 1 0 0 10 5 5 0 0 0 0-10z"/></svg>Job Search</li>
  <li><svg viewBox="0 0 24 24"><path d="M12 3l10 9h-3v9h-5v-6h-4v6H5v-9H2z"/></svg>In-House</li>
  <li><svg viewBox="0 0 24 24"><circle cx="12" cy="7" r="5"/><path d="M3 22c0-5 4-8 9-8s9 3 9 8z"/></svg>Private Practice</li>
  <li><svg viewBox="0 0 24 24"><path d="M12 3c6 0 10 3.5 10 8s-4 8-10 8c-1 0-2-.1-3-.4L4 21l1.3-4C3.2 15.5 2 13.4 2 11c0-4.5 4-8 10-8z"/></svg>Compliance</li>
</ul>

<main class="welcome abs">
  <h2>Welcome to Ridgel</h2>
  <p>This is Draftwell's version&nbsp; of Lorem Ipsum. Proin gravida nibh vel velit auctor aliquet. Aenean sollicitudin, lorem quis bibendum auctor, nisi elit consequat ipsum, nec sagittis sem nibh id elit. Duis sed odio sit amet nibh vulputate cursus a sit amet mauris. Morbi accumsan ipsum velit. Nam nec tellus a odio tincidunt auctor a ornare odio.</p>
  <p>Class aptent taciti sociosqu ad litora torquent per conubia nostra, per inceptos himenaeos. Mauris in erat justo. Nullam ac urna eu felis dapibus condimentum sit amet a augue. Sed non neque elit.</p>
</main>

<aside class="featured abs">
  <h2>Featured jobs</h2>
  <div class="job"><div class="job-title">Commercial Counsel APAC – MNC</div><div class="job-loc"><svg viewBox="0 0 8 11"><path d="M4 0a4 4 0 0 1 4 4c0 3-4 7-4 7S0 7 0 4a4 4 0 0 1 4-4zm0 2.5a1.5 1.5 0 1 0 0 3 1.5 1.5 0 0 0 0-3z"/></svg>Singapore</div></div>
  <div class="job"><div class="job-title">Contract Attorney 6 Months</div><div class="job-loc"><svg viewBox="0 0 8 11"><path d="M4 0a4 4 0 0 1 4 4c0 3-4 7-4 7S0 7 0 4a4 4 0 0 1 4-4zm0 2.5a1.5 1.5 0 1 0 0 3 1.5 1.5 0 0 0 0-3z"/></svg>Tokyo</div></div>
  <div class="job"><div class="job-title">Litigation and Regulatory Counsel</div><div class="job-loc"><svg viewBox="0 0 8 11"><path d="M4 0a4 4 0 0 1 4 4c0 3-4 7-4 7S0 7 0 4a4 4 0 0 1 4-4zm0 2.5a1.5 1.5 0 1 0 0 3 1.5 1.5 0 0 0 0-3z"/></svg>Singapore</div></div>
  <div class="job"><div class="job-title">Commercial Counsel APAC</div><div class="job-loc"><svg viewBox="0 0 8 11"><path d="M4 0a4 4 0 0 1 4 4c0 3-4 7-4 7S0 7 0 4a4 4 0 0 1 4-4zm0 2.5a1.5 1.5 0 1 0 0 3 1.5 1.5 0 0 0 0-3z"/></svg>Singapore</div></div>
</aside>

<footer class="site-footer abs"></footer>
<div class="book-art abs" role="img" aria-label="Illustration of a law book with a gavel"></div>
<div class="footer-brand abs"><span class="brand-dot"></span><span>Ridgel</span></div>
<div class="map-art abs" role="img" aria-label="Faint dotted world map decoration"></div>
<nav class="quick-links abs">
  <h3>Quick links</h3>
  <div class="link-cols">
    <ul><li>Legal Recruiting Services</li><li>Legal Career Opportunities</li><li>Legal Recruiters</li><li>Subscribe</li></ul>
    <ul><li>Legal Recruiting Services</li><li>Legal Career Opportunities</li><li>Legal Recruiters</li><li>Subscribe</li></ul>
  </div>
</nav>
<div class="footer-contact abs">
  <h3><svg viewBox="0 0 20 16" fill="none" stroke="#444" stroke-width="1.8"><rect x="1" y="1" width="18" height="14" rx="1.5"/><path d="M1.5 2l8.5 7 8.5-7"/></svg>Contact Us</h3>
  <p>Questions or comments ? <span class="write">Write to us.</span></p>
  <p class="gap">Address 1 : (65) 6555-0147</p>
  <p>Address 2 : (86) 10 5550-3926</p>
</div>

<div class="legal-bar abs">© 2014 Ridgel Legal Recrutment Limited. All Rights Reserved.</div>

</body>
</html>
```